Graphic Insert - For Pillow Case

We are purchasing new pillow cases for a campaign we are running and need a graphic insert as part of our corporate branding and product description to go in our packaging. The packaging will be a clear plastic back with this graphic insert.

Size of Flyer: 6"x9"

Description: 440 Thread Count Egyptian Cotton Pillow Cases
Quantity: 2
Size of Pillow Case: Standard
Descriptive Words: Soft, Caress, Smooth, Gentle

Our website: www.velardo.com

Thanks,

Dale

```html
<!DOCTYPE html>
<html lang="en">
<head>
<meta charset="utf-8">
<title>Velardo Pillow Case Insert</title>
<link href="https://fonts.googleapis.com/css2?family=Varela+Round&family=Josefin+Sans:wght@300;400&family=Playfair+Display:wght@700&display=swap" rel="stylesheet">
<style>
  :root {
    --backdrop: #d9d9d9;
    --paper: #ffffff;
    --photo-light: #eeeff1;
    --photo-mid: #cfd2d8;
    --teal: #5f7d84;
    --chrome-light: #f4f6f8;
    --chrome-mid: #9aa3ab;
    --chrome-dark: #3e4a52;
    --copy-grey: #9a9ea4;
    --logo-grey: #6d6f72;
  }
  * { box-sizing: border-box; margin: 0; padding: 0; }
  html, body {
    width: 1200px; height: 1000px; overflow: hidden;
    background: var(--backdrop);
  }
  .insert {
    position: absolute; left: 300px; top: 50px;
    width: 600px; height: 900px;
    background: var(--paper);
    overflow: hidden;
    box-shadow: 0 12px 30px rgba(0,0,0,0.18);
  }
  .product-photo {
    position: absolute; left: 0; top: 0; width: 600px; height: 720px;
    background:
      radial-gradient(ellipse 70% 40% at 60% 55%, var(--photo-mid), transparent 70%),
      linear-gradient(170deg, var(--photo-light) 0%, var(--photo-mid) 55%, var(--photo-light) 100%);
  }
  .headline {
    position: absolute; left: 40px; top: 60px;
    font-family: 'Varela Round', sans-serif; font-weight: 400;
    font-size: 70px; line-height: 0.92; letter-spacing: 1px;
    text-transform: uppercase;
    background: linear-gradient(180deg, var(--chrome-light) 0%, var(--chrome-mid) 45%, var(--chrome-dark) 55%, var(--chrome-light) 100%);
    -webkit-background-clip: text; background-clip: text;
    color: transparent;
    -webkit-text-stroke: 2px var(--chrome-dark);
  }
  .headline .line { display: block; }
  .headline .ampersand {
    position: absolute; left: 360px; top: 0;
    font-family: 'Playfair Display', serif;
    font-size: 190px; line-height: 1;
    -webkit-text-stroke: 2px var(--chrome-mid);
    opacity: 0.85;
  }
  .callout { position: absolute; left: 0; top: 0; }
  .feature-mark {
    position: absolute; left: 440px; top: 560px;
    width: 56px; height: 56px; border-radius: 50%;
    background: var(--teal);
  }
  .product-details {
    position: absolute; left: 40px; top: 598px;
    font-family: 'Josefin Sans', sans-serif; font-weight: 300;
    color: var(--copy-grey); text-transform: uppercase;
  }
  .product-details .title { font-size: 22px; line-height: 1.2; }
  .product-details .spec { font-size: 14px; line-height: 1.4; margin-top: 4px; }
  .web-band {
    position: absolute; left: 0; top: 760px; width: 400px; height: 70px;
    background: var(--teal);
    clip-path: polygon(0 0, 100% 0, 88% 100%, 0 100%);
    display: flex; align-items: center; padding-left: 40px;
  }
  .web-band .url {
    font-family: 'Josefin Sans', sans-serif; font-weight: 300;
    font-size: 17px; letter-spacing: 7px; text-transform: uppercase;
    color: var(--paper);
  }
  .brand {
    position: absolute; left: 352px; top: 765px;
    display: flex; align-items: center; gap: 12px;
  }
  .brand .badge {
    width: 60px; height: 60px; border-radius: 50%;
    background: var(--paper);
    border: 2px solid var(--logo-grey);
  }
  .brand .name {
    font-family: 'Josefin Sans', sans-serif; font-weight: 300;
    font-size: 26px; letter-spacing: 4px; color: var(--logo-grey);
    text-transform: uppercase; line-height: 1;
    white-space: nowrap;
  }
</style>
</head>
<body>
  <main class="insert">
    <div class="product-photo" role="img" aria-label="Close-up photograph of a white Egyptian cotton pillow case corner"></div>

    <h1 class="headline">
      <span class="line">Soft, Caress</span>
      <span class="line">Smooth</span>
      <span class="line">Gentle</span>
      <span class="ampersand">&amp;</span>
    </h1>

    <svg class="callout" width="600" height="720" viewBox="0 0 600 720" aria-hidden="true">
      <circle cx="330" cy="400" r="5" fill="var(--teal)"/>
      <polyline points="330,400 420,400 468,555" fill="none" stroke="var(--teal)" stroke-width="1.5"/>
    </svg>
    <div class="feature-mark" role="img" aria-label="Cotton flower symbol"></div>

    <div class="product-details">
      <p class="title">440 Thread Count Egyptian<br>Cotton Pillow Cases</p>
      <p class="spec">Quantity: 2<br>Size of Pillow Case: Standard</p>
    </div>

    <div class="web-band"><span class="url">www.velardo.com</span></div>

    <div class="brand">
      <span class="badge"></span>
      <span class="name">Velardo</span>
    </div>
  </main>
</body>
</html>
```